Web Design for UK Based Technology Company*

Norvexa is a new entrant in the data marketplace.
It is offering two direct API services to help clients access:
- Company Data
- Location Data
We also offer data services and consulting to help companies to integrate our API services and the data derived from them into their businesses. Our aim is to offer both the technology and services to help businesses use and integrate data better. It is a modern business built to support a modern world.

Target Market(s)

Business Professionals and decision makers

Industry/Entity Type

It Service

Number of Pages Required

5+ page

Font styles to use
Sans Serif

Colors

Designer to choose colors to be used in the design.

Requirements
Must have
• The full suite of PSD designs taking into account the layouts and wireframes supplied with which it will be compared. Focus on the homepage first. It has to have a consistent theme/feel. It has to fit with the logo.
Nice to have
• Simple, clean, a few strong ideas.
Should not have
• Cartoons, overdesign, loud colours.

```html
<!DOCTYPE html>
<html lang="en">
<head>
<meta charset="utf-8">
<title>Norvexa — Richer data to drive your business</title>
<link href="https://fonts.googleapis.com/css2?family=Lato:wght@400;700;900&family=Merriweather:wght@700&display=swap" rel="stylesheet">
<style>
:root{
  --blue:#1f9fe6;
  --blue-deep:#1789d4;
  --navy:#155685;
  --ink:#1d1d1f;
  --text:#333;
  --teal:#22d0c3;
  --teal-dark:#14506e;
  --line:#e4e6ea;
  --soft:#f8f8f9;
  --foot:#f4f5f7;
  --white:#fff;
}
*{box-sizing:border-box;margin:0;padding:0}
html,body{width:1200px;height:3292px;overflow:hidden;background:var(--white)}
body{font-family:'Lato',sans-serif;color:var(--text);position:relative}
a{color:var(--blue);text-decoration:underline}
.brand{display:flex;align-items:center;gap:10px;font-family:'Lato',sans-serif;font-weight:700;color:var(--ink);letter-spacing:.5px}
.brand-dot{width:22px;height:22px;border-radius:50%;background:var(--navy)}

/* header */
.header{position:absolute;left:0;top:0;width:1200px;height:78px;border-bottom:1px solid var(--line)}
.header .brand{position:absolute;left:75px;top:24px;font-size:28px}
.util{position:absolute;top:27px;left:756px;display:flex;align-items:center;font-size:13px;color:var(--blue)}
.util span{margin-right:24px}
.util .phone{font-weight:700}
.util .pill{margin-right:0;border:2px solid var(--blue);border-radius:18px;padding:8px 12px;font-weight:700;font-size:12px}
.nav{position:absolute;top:78px;left:0;width:1200px;height:42px;font-size:13px;color:var(--ink);letter-spacing:.3px}
.nav span{position:absolute;top:13px}

/* hero */
.hero{position:absolute;top:120px;left:0;width:1200px;height:463px;background:radial-gradient(circle at 50% 40%,#2db0ee 0%,var(--blue) 45%,var(--blue-deep) 100%)}
.hero h1{position:absolute;top:52px;width:100%;text-align:center;color:var(--white);font-weight:900;font-size:25px;letter-spacing:-.3px}
.hero-visual{position:absolute;left:405px;top:105px;width:390px;height:200px;border-radius:12px;background:radial-gradient(ellipse at 50% 45%,rgba(255,255,255,.22) 0%,rgba(255,255,255,.08) 55%,rgba(255,255,255,0) 100%)}
.card{position:absolute;top:246px;width:250px;height:173px;background:var(--teal);border:2px solid var(--navy);border-radius:14px;text-align:center}
.card p{position:absolute;top:74px;width:100%;color:var(--teal-dark);font-weight:900;font-size:13px;line-height:16px}
.card .btn{position:absolute;left:47px;top:116px;width:152px;height:38px;background:var(--teal-dark);color:var(--teal);font-weight:900;font-size:13px;line-height:38px}
.card svg{position:absolute;left:0;top:0}

/* intro */
.intro{position:absolute;top:655px;left:267px;width:655px}
.intro .lead{font-weight:700;font-size:14.5px;line-height:24px;color:var(--ink);margin-bottom:18px}
.intro p{font-size:12.5px;line-height:20px;color:var(--ink);margin-bottom:8px}

/* product blocks */
.band-company{position:absolute;top:995px;left:0;width:1200px;height:413px;background:var(--soft);border-top:1px solid var(--line)}
.visual{position:absolute}
.product h2{position:absolute;font-size:26px;font-weight:400;color:var(--blue);letter-spacing:.3px}
.product h2 b{color:var(--ink);font-weight:400}
.product .desc{position:absolute;font-size:16px;line-height:25px;color:#444}
.product .desc b{color:var(--ink);font-weight:700}
.btn-solid{position:absolute;height:34px;background:var(--blue);color:var(--white);font-weight:900;font-size:13px;text-align:center;line-height:34px;border-radius:2px}
.btn-line{position:absolute;height:34px;border:2px solid var(--blue);color:var(--blue);font-weight:900;font-size:13px;text-align:center;line-height:30px;border-radius:2px;background:var(--white)}
.badge{position:absolute;width:104px;height:104px;border-radius:50%;background:var(--blue);color:var(--white);text-align:center;font-weight:700;font-size:11px;line-height:13px;padding-top:28px}
.badge b{display:block;font-size:15px;line-height:20px;font-weight:900}

/* CTA */
.cta{position:absolute;top:1857px;left:0;width:1200px;height:271px;background:var(--navy)}
.cta .kicker{position:absolute;left:92px;top:58px;color:var(--teal);font-weight:900;font-size:13px}
.cta h3{position:absolute;left:92px;top:80px;font-family:'Merriweather',serif;font-weight:700;color:var(--white);font-size:25px;line-height:31px}
.cta .copy{position:absolute;left:472px;top:63px;width:565px;color:var(--white);font-size:17px;line-height:20px}
.cta .copy p{margin-bottom:9px}
.cta .call{position:absolute;left:546px;top:195px;width:157px;height:37px;background:var(--teal);color:var(--white);font-weight:900;font-size:12px;text-align:center;line-height:37px}
.cta .mail{position:absolute;left:759px;top:195px;width:145px;height:37px;border:2px solid var(--teal);color:var(--teal);font-weight:900;font-size:12px;text-align:center;line-height:33px}

/* bespoke */
.bespoke h3{position:absolute;left:517px;top:2200px;font-size:20px;font-weight:700;color:var(--ink)}
.bespoke h3 span{color:var(--blue)}
.bespoke .body{position:absolute;left:519px;top:2250px;width:500px;font-size:11.5px;line-height:19px;color:var(--ink)}
.bespoke .body p{margin-bottom:9px}
.rule{position:absolute;left:519px;top:2428px;width:517px;height:1px;background:#c9ccd1}
.bespoke .after{position:absolute;left:519px;top:2466px;font-size:11.5px;line-height:19px;color:var(--ink)}
.btn-bespoke{position:absolute;left:890px;top:2518px;width:146px;height:36px;background:var(--blue);color:var(--white);font-weight:900;font-size:11.5px;text-align:center;line-height:36px}

/* location */
.where h3{position:absolute;left:175px;top:2640px;font-size:17px;font-weight:900;color:var(--ink)}
.where h3 span{color:var(--blue)}
.where address{position:absolute;left:175px;top:2685px;font-style:normal;font-size:11.5px;line-height:20px;color:var(--ink)}
.where .contact{position:absolute;left:175px;top:2783px;font-size:11.5px;color:var(--ink)}
.where .send{position:absolute;left:175px;top:2888px;width:145px;height:36px;background:var(--ink);color:var(--white);font-weight:700;font-size:12.5px;text-align:center;line-height:36px}

/* footer */
.footer{position:absolute;top:2993px;left:0;width:1200px;height:299px;background:var(--foot)}
.footer .brand{position:absolute;left:139px;top:71px;font-size:22px}
.fcol{position:absolute;top:78px;font-size:10.5px;color:var(--ink)}
.fcol h4{font-size:12px;font-weight:900;margin-bottom:9px}
.fcol li{list-style:none;line-height:21.7px;color:#444}
.fbar{position:absolute;left:75px;top:247px;width:1050px;height:1px;background:var(--line)}
.fbottom{position:absolute;top:268px;left:75px;width:1048px;font-size:10px;color:var(--ink);display:flex;justify-content:space-between}
.fbottom nav span{margin-left:20px;font-weight:700}
</style>
</head>
<body>

<header class="header">
  <div class="brand"><span class="brand-dot"></span>NORVEXA</div>
  <div class="util">
    <span>CONTACT US</span>
    <span class="phone">0300 000 000</span>
    <span>LOGIN</span>
    <span class="pill">FREE TRIAL</span>
  </div>
</header>
<nav class="nav">
  <span style="left:139px">COMPANY DATA</span>
  <span style="left:295px">LOCATION DATA</span>
  <span style="left:451px">SERVICES</span>
  <span style="left:564px">ABOUT US</span>
</nav>

<section class="hero">
  <h1>RICHER DATA TO DRIVE YOUR BUSINESS</h1>
  <div class="hero-visual" role="img" aria-label="Illustration of a data hub with connection lines branching out from a central folder"></div>

  <div class="card" style="left:157px">
    <svg width="250" height="80" fill="none" stroke="#fff" stroke-width="3">
      <rect x="85" y="28" width="32" height="22"/>
      <line x1="80" y1="55" x2="122" y2="55"/>
      <line x1="92" y1="36" x2="108" y2="36" stroke-width="2"/>
      <line x1="92" y1="42" x2="104" y2="42" stroke-width="2"/>
      <g fill="#fff" stroke="#22d0c3" stroke-width="2">
        <ellipse cx="150" cy="20" rx="17" ry="6"/>
        <path d="M133 20v10c0 3 8 6 17 6s17-3 17-6V20"/>
        <path d="M133 32v10c0 3 8 6 17 6s17-3 17-6V32"/>
        <path d="M133 44v10c0 3 8 6 17 6s17-3 17-6V44"/>
      </g>
    </svg>
    <p>COMPREHENSIVE COMPANY<br>INFORMATION</p>
    <div class="btn">COMPANY API</div>
  </div>

  <div class="card" style="left:794px">
    <svg width="250" height="80" fill="none" stroke="#fff" stroke-width="3">
      <rect x="85" y="33" width="32" height="20"/>
      <line x1="80" y1="58" x2="122" y2="58"/>
      <line x1="92" y1="41" x2="108" y2="41" stroke-width="2"/>
      <path d="M139 20a10 10 0 0 1 20 0c0 9-10 20-10 20s-10-11-10-20z" fill="#fff" stroke="none"/>
      <circle cx="149" cy="20" r="4" fill="#22d0c3" stroke="none"/>
      <path d="M165 18a5 5 0 0 1 10 0c0 5-5 11-5 11s-5-6-5-11z" fill="#fff" stroke="none"/>
    </svg>
    <p>BRING MAPPING DATA<br>INTO YOUR BUSINESS</p>
    <div class="btn">LOCATION API</div>
  </div>
</section>

<section class="intro">
  <p class="lead">Norvexa is setup for connected world. A world where data is integrated, comprehensive and useful. Where systems are designed to cooperate to make businesses more efficient. For this purpose we have focused on two key areas of work - location and company data.</p>
  <p>Our <a>Postcode API</a> is the most current in the marketplace, helping anyone pinpoint a map simply by providing a postcode. This allows you to assign a location to your postcode -level business data. We also provide an <a>Address API</a>, giving you an address for any postcode along with it's coordinate on the ground. We also supply base maps for customers looking to use <a>maps on their website</a>. And we supply a wide range of <a>bespoke GIS services</a> for more specific mapping work.</p>
  <p>For company data we have restructured the Company Registry data into something more useful and practical for businesses. Just supply one or more company numbers and we can send you back <a>detailed company information</a> covering a raft of data. Better still this data can be supplied either as a file or by API so you can receive it in the format you prefer.</p>
</section>

<section class="band-company product">
  <div class="visual" role="img" aria-label="Photo of office lever-arch files standing on a shelf" style="left:0;top:90px;width:422px;height:255px;background:linear-gradient(135deg,#7d6562 0%,#6d7684 100%)"></div>
  <h2 style="left:521px;top:105px">COMPANY <b>API</b></h2>
  <div class="desc" style="left:521px;top:147px">You supply one or more company numbers -<br>we send back everything via a simple<br><b>API or CSV file</b></div>
  <div class="btn-solid" style="left:521px;top:259px;width:150px">FIND OUT MORE</div>
  <div class="btn-line" style="left:706px;top:259px;width:133px">FREE TRIAL</div>
  <div class="badge" style="left:896px;top:67px">From<br>Only<b>£29 pm</b></div>
</section>

<section class="product">
  <div class="badge" style="left:187px;top:1491px">From<br>Only<b>£29 pm</b></div>
  <h2 style="left:345px;top:1512px">LOCATION <b>API</b></h2>
  <div class="desc" style="left:345px;top:1560px">You send us a postcode we send you the location.<br>OR you send us the location, we send back the<br>postcode: <b>API or CSV file</b></div>
  <div class="btn-solid" style="left:346px;top:1680px;width:150px">FIND OUT MORE</div>
  <div class="btn-line" style="left:543px;top:1680px;width:133px">FREE TRIAL</div>
  <div class="visual" role="img" aria-label="White tablet showing a street map with location pins" style="left:830px;top:1555px;width:370px;height:265px;background:linear-gradient(135deg,#f4f5f6,#dfe2e5)"></div>
</section>

<section class="cta">
  <div class="kicker">GO AHEAD:</div>
  <h3>Test Your Data or<br>Lets's Talk it through</h3>
  <div class="copy">
    <p>If you are confident you know what you want, why not start a trial? It's free of charge and you can test the service for a limited time.</p>
    <p>If you are not so sure or you have a very specific requirements then talk to our consultants.</p>
  </div>
  <div class="call">CALL 0000 000 000</div>
  <div class="mail">SEND AN EMAIL</div>
</section>

<section class="bespoke">
  <div class="visual" role="img" aria-label="Illustration of a web form window with input fields and a submit button" style="left:143px;top:2238px;width:329px;height:287px;background:linear-gradient(180deg,#a9c6f0,#86aee6)"></div>
  <h3><span>Demanding Data Requirements?</span> Look no Further</h3>
  <div class="body">
    <p>Most businesses looking for our help have a complex data requirements they need to piece together. It may be they have an in-house team, but if not, we can help with:</p>
    <p>- Connecting our API into existing systems and software</p>
    <p>- Helping with more complex business or location data supply</p>
    <p>- Placing experienced staff on site to assist with mapping and data projects</p>
    <p>- Helping businesses automate and digitally transform</p>
  </div>
  <div class="rule"></div>
  <div class="after">So if you want us to help you take your integrations up a notch,<br>then <a>let's talk</a>.<br>Please <b>call 0000 000 000</b> or</div>
  <div class="btn-bespoke">BESPOKE SERVICES</div>
</section>

<section class="where">
  <h3><span>WHERE IS</span> NORVEXA</h3>
  <address>Second Floor, 8 Merrow Court<br>Larkfield Park<br>Ashcombe<br>Westford WF7 2QT</address>
  <div class="contact"><b>CONTACT:</b>&nbsp;&nbsp;&nbsp; 0000 000 000</div>
  <div class="send">Send an Email</div>
  <div class="visual" role="img" aria-label="Street map of the business park showing the office location" style="left:497px;top:2638px;width:528px;height:297px;background:linear-gradient(135deg,#f1f2f3,#e4e7e9);border:1px solid #d6d9dc"></div>
</section>

<footer class="footer">
  <div class="brand"><span class="brand-dot"></span>NORVEXA</div>
  <ul class="fcol" style="left:344px"><h4>COMPANY DATA</h4><li>Company Information</li><li>Alerts and Notifications</li><li>Contact Information</li><li>Financial Information</li><li>Other Data Services</li></ul>
  <ul class="fcol" style="left:553px"><h4>LOCATION DATA</h4><li>Postcode Lookup</li><li>Address Lookup</li><li>Base Mapping</li><li>Boundaries</li><li>Bespoke Mapping</li></ul>
  <ul class="fcol" style="left:762px"><h4>SERVICES</h4><li>API / Integrations</li><li>Licensing / IPR</li><li>Complex Location Data</li><li>Digital Transformation</li></ul>
  <ul class="fcol" style="left:971px"><h4>NORVEXA</h4><li>Pricing</li><li>About Us</li><li>Contact Us</li><li>Free Trial</li><li>Login</li></ul>
  <div class="fbar"></div>
  <div class="fbottom">
    <span>(c) Halden Digital Limited. All rights reserved</span>
    <nav><span>Sitemap</span><span>Terms of Use</span><span>Privacy Policy</span><span>Contact Us</span></nav>
  </div>
</footer>

</body>
</html>
```